Property Services Bi/Tri-Fold Rack Brochure

We need a 9" x 4" bi/tri-fold flyer to drop off to new customers, want to include info regarding our Property services department.
Also want to include info on the back about our other divisions.
Can have a look at our website to see what we have already done in branding etc
http://www.veltrimworks.com/index.php/propertyservices
Emphasis given to maintenance & restoration in the housing industry.
Updates

Thank you for your current design submissions, unfortunately management has changed the format to 9" x 4" Bi/Tri-Fold Rack Brochure, please update your current design if possible.

Current submissions are looking great, please be aware this particular brochure is geared towards the property services industry rather than building and construction as predominately displayed on some designs.  Property services includes internal maintenance, renovations, swap outs (old for new) etc.

Target Market(s)

New clients that we cold call or meet at events, demographic is aged 30+, most likely business to business within similar industries.

Industry/Entity Type

Industry

Requirements
Must have
• VeltrimWorks Logo (vanilla, untouched)
Common color theme based around the logo
Nice to have
• imagery of new homes, retirement villages.
Must instill confidence and a feel of longevity within the industry.
Should not have
• imagery of contractors repairing things, incomplete constructions

```html
<!DOCTYPE html>
<html lang="en">
<head>
<meta charset="utf-8">
<title>VeltrimWorks Property Services Brochure</title>
<link rel="stylesheet" href="https://fonts.googleapis.com/css2?family=Kanit:wght@300;500;600&display=swap">
<style>
  :root {
    --navy: #0d3f70;
    --green: #8cc63f;
    --ink: #2e2e2e;
    --paper: #f3f3f3;
    --paper-edge: #e4e4e4;
    --stage: #d9d9d9;
    --sky: #9fc3e6;
    --brick: #9a6a4e;
  }
  * { box-sizing: border-box; margin: 0; padding: 0; }
  html, body { width: 1200px; height: 844px; overflow: hidden; }
  body {
    background: var(--stage);
    font-family: "Kanit", sans-serif;
    color: var(--ink);
    position: relative;
  }
  .brochure {
    position: absolute;
    left: 260px; top: 39px;
    width: 680px; height: 765px;
    display: flex;
  }
  .panel {
    position: relative;
    width: 340px; height: 765px;
    background: linear-gradient(90deg, var(--paper) 0%, #fff 60%, var(--paper) 100%);
    overflow: hidden;
  }
  .panel--inside-left { border-right: 1px solid var(--paper-edge); }
  .photo {
    position: absolute; left: 0; width: 100%;
  }
  .photo--street-left {
    top: 0; height: 310px;
    background: linear-gradient(180deg, var(--sky) 0%, #c9dcef 45%, var(--brick) 62%, #b89a80 80%, #8d9a6b 100%);
  }
  .photo--street-right {
    top: 0; height: 310px;
    background: linear-gradient(180deg, #8fb7e0 0%, #c4d9ee 50%, #b9a58e 68%, #a7a39b 85%, #7d8a62 100%);
  }
  .photo--village {
    top: 440px; height: 300px;
    background: linear-gradient(180deg, #7ea9d6 0%, #d6e3ef 35%, #e8e4da 55%, #c9a98a 80%, #8e9a70 100%);
  }
  .band-curve { position: absolute; left: 0; width: 100%; display: block; }
  .band-curve--top { top: 292px; height: 44px; }
  .band-curve--photo { top: 428px; height: 30px; }
  .footer-band {
    position: absolute; left: 0; bottom: 0;
    width: 100%; height: 18px;
    background: var(--navy);
  }
  .brand {
    position: absolute; top: 26px; left: 22px;
    display: flex; align-items: center; gap: 8px;
  }
  .brand__square { width: 20px; height: 20px; background: var(--navy); }
  .brand__name {
    font-weight: 600; font-size: 28px; letter-spacing: 0.5px;
    color: var(--navy); line-height: 1;
  }
  .copy {
    position: absolute; left: 26px; right: 22px;
    font-weight: 300; font-size: 14.5px; line-height: 1.28;
  }
  .copy--intro { top: 350px; }
  .copy--closing { top: 640px; }
  .copy--team { top: 328px; left: 22px; }
  .services {
    position: absolute; top: 440px; left: 26px;
    list-style: none;
  }
  .services li {
    font-weight: 500; font-size: 15px; letter-spacing: 0.3px;
    margin-bottom: 13px;
    display: flex; align-items: center; gap: 10px;
  }
  .services li::before {
    content: ""; width: 9px; height: 9px; background: var(--navy);
    flex: none;
  }
</style>
</head>
<body>
  <main class="brochure">
    <section class="panel panel--inside-left">
      <div class="photo photo--street-left" role="img" aria-label="Photo of new brick family homes along a suburban street"></div>
      <svg class="band-curve band-curve--top" viewBox="0 0 340 44" preserveAspectRatio="none" aria-hidden="true">
        <path d="M0 12 Q170 30 340 24 L340 44 L0 44 Z" fill="#f3f3f3"/>
        <path d="M0 4 Q170 22 340 16 L340 24 Q170 30 0 12 Z" fill="var(--navy)"/>
      </svg>
      <p class="copy copy--intro">Veltrim Works can tailor a solution to meet any new or existing project’s requirements and can assist your organisation with the following services:</p>
      <ul class="services">
        <li>Refurbishments and Upgrades</li>
        <li>Cyclic Maintenance</li>
        <li>Reactive Maintenance</li>
        <li>Building risk assessments</li>
        <li>Fire Integrity Reports</li>
        <li>Access Control solutions</li>
      </ul>
      <p class="copy copy--closing">Veltrim Works has significant experience in the aged care and retirement sector. Our business can work with you to ensure that your assets are compliant and properly maintained.</p>
      <div class="footer-band"></div>
    </section>

    <section class="panel panel--inside-right">
      <div class="photo photo--street-right" role="img" aria-label="Photo of a row of new townhouses on a residential street"></div>
      <div class="brand">
        <span class="brand__square"></span>
        <span class="brand__name">VeltrimWorks</span>
      </div>
      <svg class="band-curve band-curve--top" viewBox="0 0 340 44" preserveAspectRatio="none" aria-hidden="true">
        <path d="M0 24 Q170 30 340 12 L340 44 L0 44 Z" fill="#f8f8f8"/>
        <path d="M0 16 Q170 22 340 4 L340 12 Q170 30 0 24 Z" fill="var(--navy)"/>
      </svg>
      <p class="copy copy--team">Using our experience, our dedicated team are aware of the delicate environment that exists within this sector. Our team, from executive management to tradesman are trained in how to conduct themselves in these environments.</p>
      <div class="photo photo--village" role="img" aria-label="Photo of a modern retirement village apartment building"></div>
      <svg class="band-curve band-curve--photo" viewBox="0 0 340 30" preserveAspectRatio="none" aria-hidden="true">
        <path d="M0 0 L340 0 L340 12 Q170 26 0 14 Z" fill="#f8f8f8"/>
      </svg>
      <div class="footer-band"></div>
    </section>
  </main>
</body>
</html>
```